Electrical Contracting Business Website

Require website done for my contracting business.
Partly done one but really dont have time.

You can view the current one at http://brelton.net.au

You can use any info/styles/photos from the current website

I like the orange color of the logo so id like things to be with that
Unfortunatly being a new business (Sept 2015) I havent got alot of photos . but if you require any for any of the specifics listed in the doc file ill have a look to see what I have.

I am targeting mainly commercial / industrial clients. Which also includes government and mining.

Target Market(s)

People requiring electricians

Industry/Entity Type

Electrician

Coding

Number of Pages Required

Colors
f37122

Requirements
Must have
• logo with EC Number
• Keep it simple and not to complicated
• Comply with the current html / style sheet standards.
• Desktop/Mobile Version compatability
Nice to have
• additional photos.
• The domestic lifts we install are by vostrel I dont have any photos of them unfortunately.
Should not have
• change colour of logo

```html
<!DOCTYPE html>
<html lang="en">
<head>
<meta charset="utf-8">
<title>Brelton Engineering – Specialized Electrical Services</title>
<link rel="stylesheet" href="https://fonts.googleapis.com/css2?family=Bree+Serif&family=Lilita+One&family=Open+Sans:wght@400;600;700&display=swap">
<style>
:root{
  --orange:#f37122;
  --orange-deep:#e8511f;
  --red:#c8200f;
  --ink:#2b2b2b;
  --text:#444;
  --white:#fff;
  --grey-band:#e9e9e9;
  --footer:#242424;
  --footer-text:#c9c9c9;
  --services-dark:#1c1712;
}
*{box-sizing:border-box;margin:0;padding:0}
html,body{width:1200px;height:2423px;overflow:hidden}
body{font-family:"Open Sans",Arial,sans-serif;color:var(--text);background:var(--white);position:relative}

/* Hero */
.hero{position:absolute;left:0;top:0;width:1200px;height:636px;overflow:hidden}
.hero-photo{position:absolute;inset:0;background:
  radial-gradient(ellipse 520px 220px at 560px 470px,#f59a4a 0%,#d6662c 35%,rgba(120,50,30,0) 75%),
  linear-gradient(180deg,#6f6a6e 0%,#8a7070 30%,#b5623a 62%,#5a2615 80%,#160b07 100%)}
.hero-stripe{position:absolute;inset:0}
.hero-copy{position:absolute;left:53px;top:240px;width:560px;color:var(--white)}
.hero-title{font-family:"Bree Serif",Georgia,serif;font-size:42px;line-height:44px;letter-spacing:1px;text-transform:uppercase;text-shadow:2px 2px 3px rgba(0,0,0,.55)}
.hero-sub{font-size:24px;line-height:34px;margin-top:4px;text-shadow:1px 1px 2px rgba(0,0,0,.5)}
.hero-btn{position:absolute;left:56px;top:420px;width:180px;height:44px;background:var(--white);color:var(--red);font-size:17px;font-weight:600;line-height:44px;padding-left:24px;text-transform:uppercase;clip-path:polygon(0 0,100% 0,90% 100%,0 100%)}

/* Header */
.site-header{position:absolute;left:47px;top:0;width:1153px;height:113px;background:var(--white)}
.brand{position:absolute;left:8px;top:14px;display:flex;align-items:center;gap:8px}
.brand-mark{width:40px;height:40px;border-radius:50%;background:var(--orange)}
.brand-name{font-family:"Open Sans",sans-serif;font-weight:700;font-size:30px;color:var(--orange);line-height:40px}
.brand-reg{position:absolute;left:8px;top:64px;font-size:7px;line-height:9px;color:var(--orange);font-weight:600}
.contact-chip{position:absolute;top:12px;display:flex;align-items:center;gap:14px}
.contact-chip.phone{left:672px}
.contact-chip.email{left:867px}
.chip-label{font-size:9px;letter-spacing:.5px;color:#666;text-transform:uppercase}
.chip-value{font-size:15px;font-weight:700;color:#444}
.main-nav{position:absolute;top:80px;left:526px}
.main-nav a{position:absolute;font-size:14px;color:#333;text-decoration:none;text-transform:uppercase;white-space:nowrap;padding-bottom:8px}
.main-nav a.active{border-bottom:3px solid var(--orange-deep)}

/* About */
.about{position:absolute;left:0;top:636px;width:1200px;height:443px;text-align:center}
.section-title{font-family:"Bree Serif",Georgia,serif;font-size:52px;color:var(--ink);margin-top:39px;line-height:64px}
.title-rule{width:162px;height:3px;background:var(--orange-deep);margin:10px auto 0}
.about p{width:1074px;margin:0 auto;font-size:17px;line-height:26px;color:var(--text)}
.about p.first{margin-top:24px}
.about p+p{margin-top:26px}

/* Services */
.services{position:absolute;left:0;top:1079px;width:1200px;height:436px;background:linear-gradient(135deg,#3a2a1c 0%,var(--services-dark) 60%,#0f0c0a 100%);overflow:hidden}
.services-photo{position:absolute;inset:0;clip-path:polygon(743px 0,1200px 0,1200px 436px,517px 436px);background:
  linear-gradient(180deg,#8e8b88 0%,#b49a78 35%,#d29a3a 58%,#5a3a1e 80%,#2a1e16 100%)}
.services-title{position:absolute;left:45px;top:42px;font-family:"Lilita One",sans-serif;font-size:36px;color:var(--orange-deep);letter-spacing:.5px}
.service-list{position:absolute;list-style:none;color:var(--white);font-size:19px;line-height:37px}
.service-list.col-a{left:50px;top:103px}
.service-list.col-b{left:316px;top:100px}
.service-list li{padding-left:18px;position:relative}
.service-list li::before{content:"";position:absolute;left:0;top:15px;width:7px;height:7px;background:var(--orange-deep);transform:rotate(45deg)}

/* Sectors */
.sectors{position:absolute;left:0;top:1515px;width:1200px;height:531px}
.sector-card{position:absolute;top:94px;width:339px}
.sector-card.residential{left:65px}
.sector-card.commercial{left:428px}
.sector-card.industrial{left:799px}
.sector-photo{width:339px;height:200px}
.residential .sector-photo{background:linear-gradient(160deg,#e8e8e8 0%,#bfc4c6 50%,#2a6a7a 100%)}
.commercial .sector-photo{background:linear-gradient(160deg,#d9d2c4 0%,#5a5650 45%,#1e1d1c 100%)}
.industrial .sector-photo{background:linear-gradient(180deg,#1d1d1d 0%,#e9e4d8 40%,#ef6a2a 65%,#1a1a1a 100%)}
.sector-label{position:absolute;left:21px;top:174px;width:296px;height:48px;background:var(--orange-deep);color:var(--white);font-size:22px;font-weight:600;letter-spacing:1px;text-align:center;line-height:48px;text-transform:uppercase}
.sector-text{margin-top:48px;font-size:14.5px;line-height:22px;color:#555;text-align:center;padding:0 22px}
.load-more{position:absolute;left:527px;top:439px;width:146px;height:36px;border-radius:12px;background:#111;color:var(--white);font-size:14px;display:flex;align-items:center;justify-content:center;gap:12px}

/* Call to action */
.cta{position:absolute;left:0;top:2046px;width:1200px;height:112px;background:var(--grey-band)}
.cta-text{position:absolute;left:48px;top:36px;font-size:29px;color:#333;letter-spacing:.2px}
.cta-btn{position:absolute;left:933px;top:25px;width:181px;height:52px;background:var(--orange-deep);border-radius:3px;color:var(--white);font-weight:700;font-size:18px;display:flex;align-items:center;justify-content:center;gap:12px}

/* Footer */
.site-footer{position:absolute;left:0;top:2158px;width:1200px;height:265px;background:var(--footer);color:var(--footer-text);text-align:center}
.member-badge{position:absolute;left:538px;top:22px;width:162px;height:78px;border-radius:4px;background:#4a4a4a}
.footer-contact{position:absolute;left:0;top:122px;width:1200px;font-size:16px;display:flex;justify-content:center;align-items:center;gap:10px}
.footer-contact svg{vertical-align:-2px;margin-right:4px}
.copyright{position:absolute;left:0;top:158px;width:1200px;font-size:15px}
.social{position:absolute;top:212px;width:22px;height:22px;background:#111;transform:rotate(45deg)}
</style>
</head>
<body>

<section class="hero">
  <div class="hero-photo" role="img" aria-label="Sunset photo of two electricians in hard hats standing beside an oil pump jack"></div>
  <svg class="hero-stripe" width="1200" height="636" viewBox="0 0 1200 636">
    <polygon points="468,113 640,113 355,636 137,636" fill="#c8200f" opacity=".85"/>
  </svg>
  <div class="hero-copy">
    <h1 class="hero-title">Specialized Electrical<br>Services</h1>
    <p class="hero-sub">Our mission is providing a high quality prod-<br>ucts and unsurpassed customer service</p>
  </div>
  <div class="hero-btn">Learn More</div>
</section>

<header class="site-header">
  <div class="brand">
    <span class="brand-mark"></span>
    <span class="brand-name">Brelton</span>
  </div>
  <div class="brand-reg">ACN 000 111 222<br>ABN 00 111 222 333 &nbsp; EC LIC: 40712</div>

  <div class="contact-chip phone">
    <svg width="22" height="34" viewBox="0 0 22 34" fill="none" stroke="#777" stroke-width="1.6"><rect x="2" y="1" width="18" height="32" rx="3"/><line x1="2" y1="6" x2="20" y2="6"/><line x1="2" y1="27" x2="20" y2="27"/></svg>
    <div><div class="chip-label">Call us today</div><div class="chip-value">+61 0400 217 386</div></div>
  </div>
  <div class="contact-chip email">
    <svg width="32" height="28" viewBox="0 0 32 28" fill="none" stroke="#777" stroke-width="1.6"><path d="M2 10 L16 1 L30 10 V27 H2 Z"/><path d="M2 10 L16 19 L30 10"/><rect x="8" y="5" width="16" height="10" fill="#fff"/><line x1="11" y1="9" x2="21" y2="9"/><line x1="11" y1="12" x2="19" y2="12"/></svg>
    <div><div class="chip-label">Email us now</div><div class="chip-value">info@brelton.net.au</div></div>
  </div>

  <nav class="main-nav">
    <a class="active" style="left:0">About Us</a>
    <a style="left:108px">Residential</a>
    <a style="left:234px">Commerical</a>
    <a style="left:365px">Industrial</a>
    <a style="left:485px">Contact Us</a>
  </nav>
</header>

<section class="about">
  <h2 class="section-title">About Brelton</h2>
  <div class="title-rule"></div>
  <p class="first">Lorem Ipsum is simply dummy text of the printing and typesetting industry. Lorem Ipsum has been the industry's standard dummy text ever since the 1500s, when an unknown printer took a galley of type and scrambled it to make a type specimen book. It has survived not only five centuries, but also the leap into electronic typesetting, remaining essentially unchanged. It was popularised in the 1960s with the release of Kestrafold sheets containing Lorem Ipsum passages, and more recently with desktop publishing software like Quillmark Layout including versions of Lorem Ipsum.</p>
  <p>Lorem Ipsum is simply dummy text of the printing and typesetting industry. Lorem Ipsum has been the industry's standard dummy text ever since the 1500s, when an unknown printer took a galley of type and scrambled it to make a type specimen book. It has survived not only five centuries, but also the leap into electronic typesetting.</p>
</section>

<section class="services">
  <div class="services-photo" role="img" aria-label="Offshore oil platform with cranes lit at sunset over the sea"></div>
  <h2 class="services-title">Our Services Include:</h2>
  <ul class="service-list col-a">
    <li>Electrical Installations</li>
    <li>Voice, and Data Cabling</li>
    <li>Electrical Modifications</li>
    <li>Fault Finding</li>
    <li>Panel Upgrades</li>
    <li>Security Lighting</li>
  </ul>
  <ul class="service-list col-b">
    <li>Generator Hookup</li>
    <li>Surge Protection</li>
    <li>Building Maintenance</li>
    <li>Lift Maintenance</li>
    <li>Crane/Hoist Maintenance</li>
    <li>Labour Hire</li>
  </ul>
</section>

<section class="sectors">
  <article class="sector-card residential">
    <div class="sector-photo" role="img" aria-label="Residential switchboard with circuit breakers"></div>
    <h3 class="sector-label">Residential</h3>
    <p class="sector-text">Constructor explains how you can enjoy high end flooring trends like textured wood and realistic stones with new laminate</p>
  </article>
  <article class="sector-card commercial">
    <div class="sector-photo" role="img" aria-label="Close-up of a commercial electric motor"></div>
    <h3 class="sector-label">Commerical</h3>
    <p class="sector-text">Constructor explains how you can enjoy high end flooring trends like textured wood and realistic stones with new laminate</p>
  </article>
  <article class="sector-card industrial">
    <div class="sector-photo" role="img" aria-label="Row of industrial fuse holders with orange labels"></div>
    <h3 class="sector-label">Industrial</h3>
    <p class="sector-text">Constructor explains how you can enjoy high end flooring trends like textured wood and realistic stones with new laminate</p>
  </article>
  <div class="load-more">Load More
    <svg width="22" height="10" viewBox="0 0 22 10" fill="none" stroke="#fff" stroke-width="1.6"><line x1="0" y1="5" x2="20" y2="5"/><polyline points="15,1 20,5 15,9"/></svg>
  </div>
</section>

<section class="cta">
  <p class="cta-text">If You Need Any Industrial Solution ... We Are Available For You</p>
  <div class="cta-btn">CONTACT US
    <svg width="12" height="18" viewBox="0 0 12 18" fill="none" stroke="#fff" stroke-width="3.5"><polyline points="2,2 9,9 2,16"/></svg>
  </div>
</section>

<footer class="site-footer">
  <div class="member-badge"></div>
  <div class="footer-contact">
    <span>Email: <svg width="15" height="12" viewBox="0 0 15 12" fill="none" stroke="#ddd" stroke-width="1.5"><rect x="1" y="1" width="13" height="10"/><polyline points="1,1 7.5,6.5 14,1"/></svg>info@brelton.net.au</span>
    <span>|</span>
    <span>Phone: <svg width="12" height="14" viewBox="0 0 12 14" fill="#ddd"><path d="M2 0 L5 0 L5.5 4 L3.5 5 C4 7.5 5.5 9 7.5 10 L8.5 8 L12 9 L12 12 C12 13 11 14 10 14 C4 13 0 8 0 2 C0 1 1 0 2 0 Z"/></svg>+61 0400 217 386</span>
    <span>|</span>
    <span>Fax: <svg width="16" height="14" viewBox="0 0 16 14" fill="none" stroke="#ddd" stroke-width="1.4"><rect x="4" y="1" width="8" height="4"/><rect x="1" y="5" width="14" height="6"/><rect x="4" y="9" width="8" height="4" fill="#242424"/></svg>+61 (08) 6100 4827</span>
  </div>
  <p class="copyright">Copyright © 2016 Brelton Engineering Pty Ltd All Rights Reserved EC 40712</p>
  <span class="social" style="left:511px"></span>
  <span class="social" style="left:554px"></span>
  <span class="social" style="left:598px;background:#3a3a3a"></span>
  <span class="social" style="left:642px"></span>
</footer>

</body>
</html>
```